This is for a poster that will be hanging in the window of a Men's Suit Store in the mall:
Size 4 feet wide by 6 feet high
Main point is: A sale on "Suits" or "Men's Suits" at 40%-60% off ( the 40%-60% off should be the focal point)
Some words that can be used are "Sale" or "Clearance Sale"
Some key words that can be used to make it urgent are "limited time offer" or something similar.
You can get creative, the point is for the customer to want to come into the store and buy a suit right away.
You may use a graphic (picture of a man in a suit). It is not necessary but if it looks good you can use it. (If you do use a picture, it should be of a modern fit or slim fit suit)
Sorry, the initial brief somehow got deleted from the project. Please see the updated brief.
Thanks
Reason: Project was closed for some reason, extended to give enough time to complete
Target Market(s)
Mostly Men ages 35-55
Industry/Entity Type
Store
Colors
Designer to choose colors to be used in the design.

```html
<!DOCTYPE html>
<html lang="en">
<head>
<meta charset="utf-8">
<title>Men's Suits Sale Poster</title>
<link rel="stylesheet" href="https://fonts.googleapis.com/css2?family=Arimo:wght@400;700&display=swap">
<style>
  :root {
    --frame: #000000;
    --paper: #ffffff;
    --navy: #0a0a6e;
    --sale-red: #ff2a00;
    --ink: #000000;
  }
  html, body {
    margin: 0;
    padding: 0;
    width: 820px;
    height: 1200px;
    overflow: hidden;
    background: var(--frame);
  }
  .poster {
    display: block;
    width: 820px;
    height: 1200px;
    font-family: "Arimo", Arial, sans-serif;
  }
  .poster-frame { fill: var(--frame); }
  .poster-paper { fill: var(--paper); }
  .headline { fill: var(--navy); font-size: 80px; font-weight: 400; }
  .sale-word {
    fill: var(--sale-red);
    font-size: 230px;
    font-weight: 400;
    filter: drop-shadow(3px 3px 2px rgba(0,0,0,0.55));
  }
  .discount { fill: var(--ink); font-size: 324px; font-weight: 700; }
  .off-word { fill: var(--ink); font-size: 215px; font-weight: 700; }
  .tag-shape { fill: var(--sale-red); }
  .tag-hole { fill: var(--paper); }
  .tag-line-main { fill: var(--paper); font-size: 82px; font-weight: 400; }
  .tag-line-sub { fill: var(--paper); font-size: 62px; font-weight: 400; }
</style>
</head>
<body>
<svg class="poster" viewBox="0 0 820 1200" xmlns="http://www.w3.org/2000/svg">
  <rect class="poster-frame" x="0" y="0" width="820" height="1200"/>
  <rect class="poster-paper" x="33" y="38" width="754" height="1130"/>

  <text class="headline" x="405" y="232" text-anchor="middle" textLength="662" lengthAdjust="spacingAndGlyphs">Men's Suits at</text>

  <text class="sale-word" transform="translate(228,800) rotate(-90)" x="0" y="0" textLength="505" lengthAdjust="spacingAndGlyphs">SALE</text>

  <text class="discount" x="255" y="530" textLength="508" lengthAdjust="spacingAndGlyphs">40%</text>
  <text class="discount" x="255" y="800" textLength="508" lengthAdjust="spacingAndGlyphs">60%</text>

  <text class="off-word" transform="translate(578,830) rotate(90)" x="0" y="0" textLength="240" lengthAdjust="spacingAndGlyphs">off</text>

  <g class="offer-tag">
    <polygon class="tag-shape" points="68,848 435,848 550,951 435,1055 68,1055"/>
    <circle class="tag-hole" cx="485" cy="952" r="14"/>
    <text class="tag-line-main" x="86" y="946" textLength="356" lengthAdjust="spacingAndGlyphs">Limited</text>
    <text class="tag-line-sub" x="88" y="1030" textLength="352" lengthAdjust="spacingAndGlyphs">time offer</text>
  </g>
</svg>
</body>
</html>
```